Readable, Vibrant Large Shop Front Poster for Tutoring School.

Uncluttered design for the windows of our Business.
It needs to be readable from a distance.
It will be split across two windows. I've uploaded a picture of the premises. The poster is unfortunately split in two- see the shopfront photo - It will be in the two Square windows where the balloons are now.
I've also uploaded our logo which will be used as signage/ on the roof and would like the posters to tie in with it.

What we want to stand out
Over all :
That we are a Tutoring School Specializing in Secondary/KTR Studies

On the left hand side:
- 1 hour lessons are $20 with no joining fees or contracts (casual week to week bookings)

The right hand side:
-Weekly Lessons no contracts
-Summer School
-Holiday Program
-Workshops
-KTR EXAM PREP

Need B0 size (1000mm x 1414mm)

Requirements
Must have
• It must have large clear writing.
Nice to have
• a border top and bottom of the logo swirls, We don't need the business name on this poster.
Should not have
• Not a fan of Purple or Lime Green.

```html
<!DOCTYPE html>
<html lang="en">
<head>
<meta charset="UTF-8">
<title>Study Harbor – Window Posters</title>
<link href="https://fonts.googleapis.com/css2?family=Arvo:ital,wght@0,400;0,700;1,700&family=Montserrat:wght@500&family=Oswald:wght@600&display=swap" rel="stylesheet">
<style>
  :root {
    --navy: #0e1621;
    --sky: #4aaedc;
    --amber: #eeaa2c;
    --orange: #e85a24;
    --ink: #1c1c1c;
    --price-blue: #2b3fa3;
    --white: #ffffff;
    --backdrop: #eeeeee;
  }
  * { margin: 0; padding: 0; box-sizing: border-box; }
  html, body { width: 1200px; height: 900px; overflow: hidden; background: var(--backdrop); }
  .canvas { position: relative; width: 1200px; height: 900px; }
  .poster {
    position: absolute; top: 95px; width: 507px; height: 720px;
    overflow: hidden; background: var(--navy);
  }
  .poster--left { left: 78px; }
  .poster--right { left: 615px; }
  .poster__backdrop { position: absolute; inset: 0; width: 100%; height: 100%; }
  .poster--right .poster__backdrop { transform: scaleX(-1); }

  .brand {
    position: absolute; top: 50px; display: flex; align-items: center; gap: 26px;
    font-family: "Montserrat", sans-serif; font-weight: 500; font-size: 34px;
    letter-spacing: 3px; color: var(--white);
  }
  .poster--left .brand { left: 52px; }
  .poster--right .brand { left: 42px; }
  .brand__dot { width: 70px; height: 70px; border-radius: 50%; background: var(--sky); flex: none; }

  .offer {
    position: absolute; top: 255px; left: 0; width: 100%; text-align: center;
    font-family: "Arvo", serif; font-size: 35px; line-height: 45px; color: var(--ink);
  }
  .offer__price { color: var(--price-blue); font-style: italic; font-weight: 700; }
  .offer__tag {
    position: absolute; top: 402px; left: 90px; width: 325px; height: 86px;
    background: var(--orange); border-radius: 4px; color: var(--white);
    font-family: "Arvo", serif; font-size: 30px; line-height: 36px;
    display: flex; align-items: center; justify-content: center; text-align: center;
  }

  .programs {
    position: absolute; top: 212px; left: 44px;
    font-family: "Arvo", serif; color: var(--ink);
  }
  .programs__title { font-size: 37px; line-height: 44px; font-weight: 700; position: relative; }
  .programs__bar {
    position: absolute; left: 156px; top: 20px; width: 125px; height: 16px; background: var(--orange);
  }
  .programs__sub { font-size: 35px; line-height: 46px; }
  .programs__list { list-style: none; margin-top: 6px; }
  .programs__item { font-size: 37px; line-height: 43px; display: flex; align-items: center; }
  .programs__arrow { width: 18px; height: 22px; margin-right: 8px; flex: none; }

  .call {
    position: absolute; top: 638px; display: flex; align-items: center; gap: 8px;
    font-family: "Oswald", sans-serif; font-weight: 600; font-size: 38px; color: var(--sky);
    letter-spacing: 1px;
  }
  .poster--left .call { left: 30px; }
  .poster--right .call { left: 295px; }
  .call__icon { width: 34px; height: 34px; }

  .photo { position: absolute; border-radius: 4px 4px 0 0; }
  .photo--students {
    left: 242px; top: 605px; width: 240px; height: 115px;
    background: linear-gradient(180deg, #c99f84 0%, #6f8fb0 55%, #3f6d92 100%);
  }
  .photo--paint {
    left: 5px; top: 630px; width: 275px; height: 90px;
    background: linear-gradient(90deg, #d9895b 0%, #e6b35a 35%, #5f93c4 70%, #3b9fa6 100%);
  }
</style>
</head>
<body>
<main class="canvas">

  <section class="poster poster--left">
    <svg class="poster__backdrop" viewBox="0 0 507 720" role="img" aria-label="Soft blurred classroom background">
      <defs>
        <linearGradient id="roomLeft" x1="0" y1="0" x2="1" y2="1">
          <stop offset="0" stop-color="#e9d5b8"/>
          <stop offset="0.35" stop-color="#eef0e4"/>
          <stop offset="0.7" stop-color="#f3e6d6"/>
          <stop offset="1" stop-color="#d9b48c"/>
        </linearGradient>
      </defs>
      <rect x="0" y="100" width="507" height="520" fill="url(#roomLeft)"/>
      <path d="M0,170 C80,175 130,225 210,215 C290,205 340,160 507,150 L507,0 L0,0 Z" fill="var(--amber)"/>
      <path d="M0,160 C80,162 125,210 205,200 C285,190 330,145 507,138 L507,0 L0,0 Z" fill="var(--sky)"/>
      <path d="M0,140 C80,140 120,190 200,182 C280,174 320,130 507,125 L507,0 L0,0 Z" fill="var(--navy)"/>
      <path d="M0,545 C90,545 150,600 250,598 C350,596 400,520 507,505 L507,720 L0,720 Z" fill="var(--amber)"/>
      <path d="M0,555 C90,556 150,612 250,610 C350,608 400,535 507,522 L507,720 L0,720 Z" fill="var(--sky)"/>
      <path d="M0,575 C90,576 150,628 250,626 C350,624 400,555 507,545 L507,720 L0,720 Z" fill="var(--navy)"/>
    </svg>

    <div class="brand"><span class="brand__dot"></span>STUDY HARBOR</div>

    <p class="offer">1 hour lessons are<br><span class="offer__price">$20</span> with no joining<br>fees or contracts</p>
    <p class="offer__tag">Casual week to<br>week bookings</p>

    <div class="call">
      <svg class="call__icon" viewBox="0 0 34 34" aria-hidden="true">
        <circle cx="17" cy="17" r="15" fill="none" stroke="var(--sky)" stroke-width="3"/>
        <path d="M11,9 l4,0 l1,5 l-2.5,1.5 c1,2.5 3,4.5 5.5,5.5 l1.5,-2.5 l5,1 l0,4 c-8,1 -15,-6 -14.5,-14.5 z" fill="var(--sky)"/>
      </svg>
      CALL US
    </div>

    <div class="photo photo--students" role="img" aria-label="Photo of a group of smiling school students holding books"></div>
  </section>

  <section class="poster poster--right">
    <svg class="poster__backdrop" viewBox="0 0 507 720" role="img" aria-label="Soft blurred classroom background">
      <defs>
        <linearGradient id="roomRight" x1="1" y1="0" x2="0" y2="1">
          <stop offset="0" stop-color="#eef0ea"/>
          <stop offset="0.4" stop-color="#f4f1ea"/>
          <stop offset="0.75" stop-color="#efe0c8"/>
          <stop offset="1" stop-color="#d8b48a"/>
        </linearGradient>
      </defs>
      <rect x="0" y="100" width="507" height="520" fill="url(#roomRight)"/>
      <path d="M0,170 C80,175 130,225 210,215 C290,205 340,160 507,150 L507,0 L0,0 Z" fill="var(--amber)"/>
      <path d="M0,160 C80,162 125,210 205,200 C285,190 330,145 507,138 L507,0 L0,0 Z" fill="var(--sky)"/>
      <path d="M0,140 C80,140 120,190 200,182 C280,174 320,130 507,125 L507,0 L0,0 Z" fill="var(--navy)"/>
      <path d="M0,545 C90,545 150,600 250,598 C350,596 400,520 507,505 L507,720 L0,720 Z" fill="var(--amber)"/>
      <path d="M0,555 C90,556 150,612 250,610 C350,608 400,535 507,522 L507,720 L0,720 Z" fill="var(--sky)"/>
      <path d="M0,575 C90,576 150,628 250,626 C350,624 400,555 507,545 L507,720 L0,720 Z" fill="var(--navy)"/>
    </svg>

    <div class="brand">STUDY HARBOR<span class="brand__dot"></span></div>

    <div class="programs">
      <p class="programs__title">Weekly<span class="programs__bar"></span></p>
      <p class="programs__sub">lessons no contracts</p>
      <ul class="programs__list">
        <li class="programs__item"><svg class="programs__arrow" viewBox="0 0 18 22" aria-hidden="true"><path d="M2,2 L16,11 L2,20 L6,11 Z" fill="var(--orange)"/></svg>Summer School</li>
        <li class="programs__item"><svg class="programs__arrow" viewBox="0 0 18 22" aria-hidden="true"><path d="M2,2 L16,11 L2,20 L6,11 Z" fill="var(--orange)"/></svg>Holiday Program</li>
        <li class="programs__item"><svg class="programs__arrow" viewBox="0 0 18 22" aria-hidden="true"><path d="M2,2 L16,11 L2,20 L6,11 Z" fill="var(--orange)"/></svg>Workshops</li>
        <li class="programs__item"><svg class="programs__arrow" viewBox="0 0 18 22" aria-hidden="true"><path d="M2,2 L16,11 L2,20 L6,11 Z" fill="var(--orange)"/></svg>KTR EXAM PREP</li>
      </ul>
    </div>

    <div class="photo photo--paint" role="img" aria-label="Photo of children holding up paint-covered hands"></div>

    <div class="call">
      <svg class="call__icon" viewBox="0 0 34 34" aria-hidden="true">
        <circle cx="17" cy="17" r="15" fill="none" stroke="var(--sky)" stroke-width="3"/>
        <path d="M11,9 l4,0 l1,5 l-2.5,1.5 c1,2.5 3,4.5 5.5,5.5 l1.5,-2.5 l5,1 l0,4 c-8,1 -15,-6 -14.5,-14.5 z" fill="var(--sky)"/>
      </svg>
      CALL US
    </div>
  </section>

</main>
</body>
</html>
```